Cosmetic injections clinic needs a fresh looking business card

We need a business card using the supplied logo and color scheme to attract future clients to our clinic. It should be modern and fresh, eye catching and not too busy. Simple and to the point is best. I would like two sided designs with the front indicating address and contact information, and the back in full color with white logo and descriptive information also provided.
Target Market(s)
Clients looking for non surgical beauty enhancements.
Contact Information for Business Card
MeloraSkin
14, 618 Birchmont Way
Larkmoor, Alberta
K2P 7W3
Phone: 555-412-6630
Email: info@meloraskin.com
Requirements
Must have
- -Logo supplied with the name and address of the clinic
- -Back of card in full color with white logo with A small line of text indicating both of the following: Anti aging consultants and cosmetic injectables
- Located inside the Voyager Wellness Group

```html
<!DOCTYPE html>
<html lang="en">
<head>
<meta charset="utf-8">
<title>MeloraSkin — Business Card</title>
<link href="https://fonts.googleapis.com/css2?family=Open+Sans:wght@400;600&display=swap" rel="stylesheet">
<style>
  :root {
    --stage: #161616;
    --card-dark: #272727;
    --card-light: #3a3a3a;
    --purple: #6b3d9e;
    --pink: #d6408f;
    --teal: #1fae98;
    --text: #ececec;
  }
  * { margin: 0; padding: 0; box-sizing: border-box; }
  html, body {
    width: 1200px; height: 1200px; overflow: hidden;
    background: var(--stage);
    font-family: "Open Sans", sans-serif;
  }
  .stage {
    width: 1200px; height: 1200px;
    display: flex; flex-direction: column; align-items: center; justify-content: center;
    gap: 36px;
  }
  .card {
    position: relative;
    width: 900px; height: 514px;
    border-radius: 6px;
    background: radial-gradient(ellipse at 55% 40%, var(--card-light), var(--card-dark) 75%);
    box-shadow: 0 18px 40px rgba(0,0,0,.55);
    overflow: hidden;
  }
  .brand {
    display: flex; align-items: center; gap: 16px;
    color: var(--purple); font-weight: 600; letter-spacing: .5px;
  }
  .brand-dot { border-radius: 50%; background: var(--pink); flex: none; }

  /* front */
  .front .brand { position: absolute; left: 80px; top: 150px; font-size: 58px; }
  .front .brand-dot { width: 26px; height: 26px; }
  .divider {
    position: absolute; left: 492px; top: 120px;
    width: 2px; height: 200px; background: var(--teal);
  }
  .contact {
    position: absolute; left: 530px; top: 128px;
    color: var(--text); font-size: 21px; line-height: 1.5;
  }
  .contact .clinic { color: var(--pink); font-size: 22px; }
  .contact .line { display: flex; align-items: center; gap: 12px; }
  .contact .lines-gap { height: 14px; }
  .contact svg { width: 20px; height: 20px; fill: var(--pink); flex: none; }
  .tagline {
    position: absolute; left: 80px; top: 370px;
    color: var(--text); font-size: 21px; line-height: 1.55;
  }

  /* back */
  .back { display: flex; align-items: center; justify-content: center; }
  .back .brand { font-size: 92px; gap: 24px; }
  .back .brand-dot { width: 40px; height: 40px; }
</style>
</head>
<body>
<main class="stage">
  <section class="card front" aria-label="Card front">
    <div class="brand"><span class="brand-dot"></span>MeloraSkin</div>
    <div class="divider"></div>
    <div class="contact">
      <div class="clinic">MeloraSkin</div>
      <div>14, 618 Birchmont Way</div>
      <div>Larkmoor, Albert K2P 7W3</div>
      <div class="lines-gap"></div>
      <div class="line">
        <svg viewBox="0 0 24 24" aria-hidden="true"><path d="M6.6 10.8a15.1 15.1 0 0 0 6.6 6.6l2.2-2.2c.3-.3.7-.4 1-.2 1.1.4 2.3.6 3.6.6.6 0 1 .4 1 1V20c0 .6-.4 1-1 1A17 17 0 0 1 3 4c0-.6.4-1 1-1h3.5c.6 0 1 .4 1 1 0 1.3.2 2.5.6 3.6.1.3 0 .7-.2 1z"/></svg>
        <span>555-412-6630</span>
      </div>
      <div class="line">
        <svg viewBox="0 0 24 24" aria-hidden="true"><path d="M2 5h20v14H2zM4 7v.4l8 5 8-5V7zm0 2.8V17h16V9.8l-8 5z"/></svg>
        <span>info@meloraskin.com</span>
      </div>
    </div>
    <p class="tagline">Anti aging consultants and cosmetic injectables<br>Located inside the Voyager Wellness Group</p>
  </section>

  <section class="card back" aria-label="Card back">
    <div class="brand"><span class="brand-dot"></span>MeloraSkin</div>
  </section>
</main>
</body>
</html>
```